Design a helpdesk ticketing platform *

We are launching a helpdesk ticketing platform. Very much like lumidesk.example, brightowl.example, calmhub.example, tidyqueue.example etc. We have a full mid-fidelity prototype built and we want someone to build the full fidelity of the product.

You can view the full mid-fidelity prototype here: https://shortlink.example/Qw8pLk

The best way moving forward is to just design the following 4 pages

- Main Dashboard https://shortlink.example/48vRxN
- All tickets https://shortlink.example/jbdYsW
- Viewing a ticket https://shortlink.example/mHqLtB
- Contacts https://shortlink.example/yKeoPd

Target Market(s)

Small business owners

Industry/Entity Type

Saas

Number of Pages Required

4 page

Font styles to use
Serif
Sans Serif

Colors

Designer to choose colors to be used in the design.

Requirements
Must have
• Must follow the prototype exactly. We are not looking for any UX changes. We want the designe xactly as the prototype is. We are only looking for design ideas.
Should not have
• modern, clean. We'd love to see the primary color as yellow, purple, orange, green or blue. You choose which one you think looks best and go with that.

```html
<!DOCTYPE html>
<html lang="en">
<head>
<meta charset="utf-8">
<title>Supportnest · Dashboard</title>
<link href="https://fonts.googleapis.com/css2?family=Nunito+Sans:wght@400;600;700;800&display=swap" rel="stylesheet">
<style>
:root{
  --brand-yellow:#ffcc00;
  --brand-mark:#4b1b50;
  --sidebar:#4b1b50;
  --sidebar-active:#2a0d2d;
  --sidebar-line:#6a3a70;
  --sidebar-icon:#c9a8cf;
  --sidebar-text:#e6d6e8;
  --topbar:#ffffff;
  --title-grey:#555555;
  --stage-light:#4a4a4a;
  --stage-dark:#0e0e0e;
  --tile-open:#00c8c8;
  --tile-due:#ff9900;
  --tile-unassigned:#9966cc;
  --tile-overdue:#bb0000;
  --tile-hold:#009966;
  --tile-unresolved:#3399ff;
  --card:#ffffff;
  --accent:#7a2a80;
  --text:#222222;
  --text-soft:#444444;
  --rule:#cfcfcf;
}
*{box-sizing:border-box;margin:0;padding:0}
html,body{width:1200px;height:766px;overflow:hidden}
body{font-family:"Nunito Sans",Arial,sans-serif;color:var(--text);position:relative;background:var(--stage-dark)}

.topbar{position:absolute;left:0;top:0;width:1200px;height:48px;background:var(--topbar)}
.brand{position:absolute;left:0;top:0;width:180px;height:48px;background:var(--brand-yellow);display:flex;align-items:center;justify-content:space-between;padding:0 14px 0 17px}
.brand-lockup{display:flex;align-items:center;gap:8px}
.brand-square{width:12px;height:12px;background:var(--brand-mark)}
.brand-name{font-weight:600;font-size:16px;color:var(--brand-mark);letter-spacing:.3px}
.page-title{position:absolute;left:198px;top:12px;font-size:18px;color:var(--title-grey);font-weight:400}
.search{position:absolute;left:928px;top:7px;width:194px;height:32px;border:1.5px solid #bdbdbd;border-radius:6px;display:flex;align-items:center;justify-content:space-between;padding:0 8px 0 11px;font-size:13px;color:#444}
.avatar{position:absolute;left:1136px;top:8px;width:31px;height:31px;border-radius:50%;background:#e3e3e3;color:#fff;font-size:13px;font-weight:700;display:flex;align-items:center;justify-content:center}
.kebab{position:absolute;left:1179px;top:12px}

.sidebar{position:absolute;left:0;top:48px;width:180px;height:718px;background:var(--sidebar)}
.new-ticket{position:absolute;left:19px;top:24px;width:142px;height:34px;border:1.5px solid #fff;border-radius:7px;color:#fff;font-size:12px;font-weight:800;display:flex;align-items:center;justify-content:space-between;padding:0 10px 0 16px}
.nav-item{position:absolute;left:0;width:180px;height:113px;border-top:1.5px solid var(--sidebar-line);display:flex;flex-direction:column;align-items:center;justify-content:center;gap:10px;color:var(--sidebar-text);font-size:13.5px;font-weight:600;letter-spacing:.2px}
.nav-item.active{background:var(--sidebar-active)}
.nav-item .caret{display:inline-block;margin-left:6px;border-left:5px solid transparent;border-right:5px solid transparent;border-top:6px solid var(--sidebar-text);vertical-align:2px}
.nav-end{position:absolute;left:0;width:180px;border-top:1.5px solid var(--sidebar-line)}

.stage{position:absolute;left:180px;top:48px;width:1020px;height:718px;background:radial-gradient(ellipse at 30% 0%,var(--stage-light) 0%,#262626 55%,var(--stage-dark) 100%)}
.greeting{position:absolute;left:196px;top:74px;font-size:25px;font-weight:600;color:#e8e8e8}

.stats{position:absolute;left:198px;top:128px;width:945px;height:93px;display:flex}
.stat{flex:1;display:flex;flex-direction:column;align-items:center;justify-content:center;color:#fff}
.stat-value{font-size:29px;font-weight:800;line-height:1}
.stat-label{font-size:12.5px;font-weight:700;margin-top:4px}
.stat.open{background:var(--tile-open)}
.stat.due{background:var(--tile-due)}
.stat.unassigned{background:var(--tile-unassigned)}
.stat.overdue{background:var(--tile-overdue)}
.stat.hold{background:var(--tile-hold)}
.stat.unresolved{background:var(--tile-unresolved)}

.activity-card{position:absolute;left:198px;top:246px;width:945px;height:486px;background:var(--card)}
.card-title{position:absolute;left:40px;top:40px;font-size:16.5px;font-weight:600;color:var(--accent)}
.card-rule{position:absolute;left:38px;top:72px;width:870px;border-top:1px solid var(--rule)}
.timeline-line{position:absolute;left:47px;top:107px;height:365px;border-left:1px solid var(--rule)}
.day-dot{position:absolute;left:38px;width:19px;height:19px;border-radius:50%;border:3.5px solid var(--accent);background:#fff}
.day-label{position:absolute;left:78px;font-size:15px;font-weight:600;color:#111}
.entry{position:absolute;left:78px;width:830px;height:58px;padding:10px 0 0 20px;font-size:15px;color:var(--text-soft);line-height:19px}
.entry.ruled{border-bottom:1px solid var(--rule)}
.entry .chev{position:absolute;left:2px;top:14px}
</style>
</head>
<body>

<header class="topbar">
  <div class="brand">
    <span class="brand-lockup"><span class="brand-square"></span><span class="brand-name">Supportnest</span></span>
    <svg width="18" height="14" viewBox="0 0 18 14"><path d="M0 1h18M4 7h14M0 13h18" stroke="#4b1b50" stroke-width="1.8"/></svg>
  </div>
  <h1 class="page-title">Dashboard</h1>
  <div class="search">
    <span>Search</span>
    <svg width="20" height="20" viewBox="0 0 20 20"><circle cx="8" cy="8" r="6" fill="none" stroke="#333" stroke-width="2.4"/><path d="M12.5 12.5l6 6" stroke="#333" stroke-width="2.8" stroke-linecap="round"/></svg>
  </div>
  <div class="avatar">DW</div>
  <svg class="kebab" width="8" height="22" viewBox="0 0 8 22"><circle cx="4" cy="3" r="2.6" fill="#999"/><circle cx="4" cy="11" r="2.6" fill="#999"/><circle cx="4" cy="19" r="2.6" fill="#999"/></svg>
</header>

<nav class="sidebar">
  <div class="new-ticket">
    <span>NEW TICKET</span>
    <svg width="6" height="24" viewBox="0 0 6 24"><circle cx="3" cy="4" r="2.4" fill="#fff"/><circle cx="3" cy="12" r="2.4" fill="#fff"/><circle cx="3" cy="20" r="2.4" fill="#fff"/></svg>
  </div>

  <div class="nav-item active" style="top:80px">
    <svg width="50" height="46" viewBox="0 0 50 46" fill="none" stroke="#c9a8cf" stroke-width="3"><path d="M7 36A21 21 0 1 1 43 36"/><path d="M25 9v4M12 16l3 3M38 16l-3 3M8 28h4M38 28h4"/><path d="M17 20l10 10"/><rect x="16" y="40" width="18" height="4" fill="#c9a8cf" stroke="none"/></svg>
    <span>DASHBOARD</span>
  </div>
  <div class="nav-item" style="top:193px">
    <svg width="50" height="46" viewBox="0 0 50 46" fill="none" stroke="#c9a8cf" stroke-width="2.4"><path d="M14 4l30 14-12 26L2 30z" fill="#c9a8cf" fill-opacity=".25"/><path d="M22 12l-8 16M28 15l-8 16M34 18l-8 16" stroke-dasharray="3 3"/></svg>
    <span>TICKETS<i class="caret"></i></span>
  </div>
  <div class="nav-item" style="top:306px">
    <svg width="50" height="48" viewBox="0 0 50 48"><circle cx="25" cy="14" r="12" fill="#c9a8cf"/><path d="M2 48c0-14 10-20 23-20s23 6 23 20z" fill="#c9a8cf"/></svg>
    <span>CONTACTS</span>
  </div>
  <div class="nav-item" style="top:420px">
    <svg width="50" height="50" viewBox="0 0 50 50"><g fill="#c9a8cf"><circle cx="25" cy="25" r="16"/><rect x="20" y="2" width="10" height="10" rx="2"/><rect x="20" y="38" width="10" height="10" rx="2"/><rect x="2" y="20" width="10" height="10" rx="2"/><rect x="38" y="20" width="10" height="10" rx="2"/><g transform="rotate(45 25 25)"><rect x="20" y="2" width="10" height="10" rx="2"/><rect x="20" y="38" width="10" height="10" rx="2"/><rect x="2" y="20" width="10" height="10" rx="2"/><rect x="38" y="20" width="10" height="10" rx="2"/></g></g><circle cx="25" cy="25" r="6" fill="#4b1b50"/></svg>
    <span>ADMIN SETTINGS<i class="caret"></i></span>
  </div>
  <div class="nav-item" style="top:533px">
    <svg width="50" height="38" viewBox="0 0 50 38" fill="none" stroke="#c9a8cf" stroke-width="3"><rect x="2" y="2" width="46" height="34" rx="4"/><path d="M2 12h46" stroke-width="5"/><path d="M8 26h14M26 26h6"/></svg>
    <span>ACCOUNT &amp; BILLING</span>
  </div>
  <div class="nav-end" style="top:646px"></div>
</nav>

<main class="stage-wrap">
  <div class="stage"></div>
  <h2 class="greeting">Good Morning, Daniel</h2>

  <section class="stats">
    <div class="stat open"><span class="stat-value">16</span><span class="stat-label">Open Tickets</span></div>
    <div class="stat due"><span class="stat-value">14</span><span class="stat-label">Due Today</span></div>
    <div class="stat unassigned"><span class="stat-value">14</span><span class="stat-label">Unassigned</span></div>
    <div class="stat overdue"><span class="stat-value">0</span><span class="stat-label">Over Due</span></div>
    <div class="stat hold"><span class="stat-value">0</span><span class="stat-label">On Hold</span></div>
    <div class="stat unresolved"><span class="stat-value">11</span><span class="stat-label">Not Resolved</span></div>
  </section>

  <section class="activity-card">
    <h3 class="card-title">Recent Activities</h3>
    <div class="card-rule"></div>
    <div class="timeline-line"></div>

    <div class="day-dot" style="top:98px"></div>
    <div class="day-label" style="top:98px">Today</div>

    <div class="entry ruled" style="top:126px">
      <svg class="chev" width="9" height="13" viewBox="0 0 9 13"><path d="M1.5 1.5l5 5-5 5" fill="none" stroke="#444" stroke-width="2.4"/></svg>
      4:49 pm<br>Marcus Hale assigned forgot to cc, trying again (#15) to Marcus Hale
    </div>
    <div class="entry ruled" style="top:184px">
      <svg class="chev" width="9" height="13" viewBox="0 0 9 13"><path d="M1.5 1.5l5 5-5 5" fill="none" stroke="#444" stroke-width="2.4"/></svg>
      10:49 am<br>Marcus Hale assigned forgot to cc, trying again (#15) to Marcus Hale
    </div>
    <div class="entry ruled" style="top:242px">
      <svg class="chev" width="9" height="13" viewBox="0 0 9 13"><path d="M1.5 1.5l5 5-5 5" fill="none" stroke="#444" stroke-width="2.4"/></svg>
      9:49 am<br>Marcus Hale added a note to the Ticket Test From Email (#12)
    </div>

    <div class="day-dot" style="top:329px"></div>
    <div class="day-label" style="top:329px">Yesterday</div>

    <div class="entry ruled" style="top:356px">
      <svg class="chev" width="9" height="13" viewBox="0 0 9 13"><path d="M1.5 1.5l5 5-5 5" fill="none" stroke="#444" stroke-width="2.4"/></svg>
      5:49 pm<br>Marcus Hale assigned test (#15)
    </div>
    <div class="entry" style="top:414px">
      <svg class="chev" width="9" height="13" viewBox="0 0 9 13"><path d="M1.5 1.5l5 5-5 5" fill="none" stroke="#444" stroke-width="2.4"/></svg>
      12:00 pm<br>Lina Park raised a new ticket test (#16)
    </div>
  </section>
</main>

</body>
</html>
```